Looking for a high-end business card design for a construction company

We are looking to update our business card design. We are a post-frame construction company that builds custom buildings, commercial spaces, homes, and anything else. We have multiple people working here so we would need something we can easily customize the information for the specific person. We need a name, website, cell phone, office phone as well as social icons. Our colors are black, white, and grey/silver so I would love a black background or something that is more striking than just a traditional white business card. Looking for something that is very professional with a high-end look/feel. I have attached our logos, they can be silver, white, grey, or black.
Industry/Entity Type
Construction
Contact Information for Business Card
Business logo, Name, Cell phone, Office phone, website, social Icons
Colors
Designer to choose only greyscale colors for use in the design.
Look and feel

```html
<!DOCTYPE html>
<html lang="en">
<head>
<meta charset="utf-8">
<title>Corvane Builders – Business Card</title>
<link href="https://fonts.googleapis.com/css2?family=Open+Sans:wght@400;600;700&display=swap" rel="stylesheet">
<style>
  :root {
    --ink: #2f2c2d;
    --ink-soft: #3a3738;
    --band-grey: #5d5d5f;
    --paper: #ffffff;
    --stage-top: #c9c9c9;
    --stage-bottom: #9d9d9d;
    --social: #8a8a8c;
  }
  * { box-sizing: border-box; margin: 0; padding: 0; }
  html, body { width: 1200px; height: 815px; overflow: hidden; }
  body {
    font-family: "Open Sans", Arial, sans-serif;
    background: linear-gradient(160deg, var(--stage-top), var(--stage-bottom));
    position: relative;
    color: var(--ink);
  }
  .card {
    position: absolute;
    width: 520px;
    height: 297px;
    background: var(--paper);
    border-radius: 18px;
    overflow: hidden;
    box-shadow: 0 14px 30px rgba(0,0,0,.28);
  }
  .card__wave { position: absolute; inset: 0; width: 100%; height: 100%; }
  .card--front { left: 60px; top: 110px; }
  .card--back { left: 620px; top: 410px; }

  .person { position: absolute; left: 34px; top: 52px; }
  .person__name { font-size: 27px; font-weight: 700; letter-spacing: .2px; line-height: 1.1; }
  .person__title { font-size: 13px; font-weight: 400; margin-top: 2px; }

  .contact { position: absolute; left: 34px; top: 130px; list-style: none; }
  .contact__item { display: flex; align-items: flex-start; gap: 12px; margin-bottom: 8px; }
  .contact__icon {
    flex: none; width: 22px; height: 22px; border-radius: 50%;
    background: var(--ink); display: flex; align-items: center; justify-content: center;
    margin-top: 2px;
  }
  .contact__text { font-size: 12.5px; line-height: 1.3; }

  .divider { position: absolute; left: 258px; top: 90px; width: 1px; }
  .divider span { position: absolute; background: var(--ink); height: 1.5px; }

  .brand {
    position: absolute; display: flex; align-items: center; gap: 10px;
    font-weight: 700; color: var(--ink); text-transform: uppercase; line-height: 1.05;
  }
  .brand__mark { flex: none; border-radius: 50%; background: var(--ink); }
  .card--front .brand { right: 40px; top: 40px; font-size: 19px; letter-spacing: 1.5px; }
  .card--front .brand__mark { width: 34px; height: 34px; }
  .card--back .brand { left: 150px; top: 72px; font-size: 36px; letter-spacing: 3px; }
  .card--back .brand__mark { width: 62px; height: 62px; }
  .brand__sub { display: block; font-size: .62em; letter-spacing: 3px; }

  .social { position: absolute; right: 60px; top: 104px; display: flex; gap: 7px; }
  .social__dot { width: 15px; height: 15px; border-radius: 50%; background: var(--social); }
</style>
</head>
<body>

  <section class="card card--front" aria-label="Business card, contact side">
    <svg class="card__wave" viewBox="0 0 520 297" preserveAspectRatio="none" aria-hidden="true">
      <path d="M0 268 C120 262 230 250 310 190 C380 138 420 90 520 72 L520 297 L0 297 Z" fill="var(--band-grey)"/>
      <path d="M0 280 C130 276 240 262 318 202 C388 150 428 104 520 88 L520 297 L0 297 Z" fill="var(--ink)"/>
    </svg>

    <div class="person">
      <h1 class="person__name">Dara Whitlock</h1>
      <p class="person__title">Founder</p>
    </div>

    <ul class="contact">
      <li class="contact__item">
        <span class="contact__icon">
          <svg width="10" height="12" viewBox="0 0 10 12"><rect x="1.5" y="0.5" width="7" height="11" rx="1.2" fill="none" stroke="#fff"/><circle cx="5" cy="9.5" r=".7" fill="#fff"/></svg>
        </span>
        <span class="contact__text">+012 345 6789<br>+012 3456 7890</span>
      </li>
      <li class="contact__item">
        <span class="contact__icon">
          <svg width="12" height="12" viewBox="0 0 12 12" fill="none" stroke="#fff"><circle cx="6" cy="6" r="5"/><ellipse cx="6" cy="6" rx="2.2" ry="5"/><path d="M1 6h10"/></svg>
        </span>
        <span class="contact__text">info@youremail.com<br>www.yourwebsite.com</span>
      </li>
      <li class="contact__item">
        <span class="contact__icon">
          <svg width="10" height="12" viewBox="0 0 10 12"><path d="M5 11.5C2 7.8 1 6 1 4.3a4 4 0 0 1 8 0C9 6 8 7.8 5 11.5Z" fill="#fff"/><circle cx="5" cy="4.3" r="1.4" fill="var(--ink)"/></svg>
        </span>
        <span class="contact__text">Alder St. No. 88/001,<br>floor Name - 9100</span>
      </li>
    </ul>

    <div class="divider" aria-hidden="true">
      <span style="left:0;top:0;width:140px;"></span>
      <span style="left:20px;top:12px;width:100px;"></span>
      <span style="left:6px;top:24px;width:90px;"></span>
    </div>

    <div class="brand">
      <span class="brand__mark" aria-hidden="true"></span>
      <span>Corvane<span class="brand__sub">Builders, Inc.</span></span>
    </div>

    <div class="social" aria-label="Social profiles">
      <span class="social__dot"></span>
      <span class="social__dot"></span>
      <span class="social__dot"></span>
      <span class="social__dot"></span>
      <span class="social__dot"></span>
      <span class="social__dot"></span>
    </div>
  </section>

  <section class="card card--back" aria-label="Business card, brand side">
    <svg class="card__wave" viewBox="0 0 520 297" preserveAspectRatio="none" aria-hidden="true">
      <path d="M0 262 C70 250 120 220 190 205 C300 182 420 178 520 130 L520 297 L0 297 Z" fill="var(--band-grey)"/>
      <path d="M0 275 C70 264 125 232 195 218 C305 196 425 192 520 146 L520 297 L0 297 Z" fill="var(--ink)"/>
    </svg>

    <div class="brand">
      <span class="brand__mark" aria-hidden="true"></span>
      <span>Corvane<span class="brand__sub">Builders, Inc.</span></span>
    </div>
  </section>

</body>
</html>
```